Stress Fracture Infographic for Scientific Paper

We need an infographic for a research/scientific paper. We would like the infographic to give readers a clear and eye-catching overview about the factors that put athletes and military personnel at risk for stress fractures. The design needs to communicate that the risk factors are cumulative and interactive; however, how they specifically accumulate and interact has not been studied or shown in the literature (we need healthcare providers who subjectively assess cumulative risk profiles in athletes and we concurrently need scientists to evaluate the interdependence of risk factors). We define cumulative risk profile as: a subjective clinical determination of the number of factors putting an athlete at risk along with thoughtful consideration regarding how all the risk factors interact with one another. We would like the infographic to display this cumulative risk profile idea.

The risk factors can be categorized as:
INTRINSIC-
Non-modifiable (such as sex, race, age, genetics, anatomical structure, and prior bone stress injury), modifiable (muscle strength, muscle fatigue, flexibility, biomechanics, stress, recovery strategies, nutrition, energy deficiency), unclear if modifiable, not, or somewhere in between (such as gut health);

EXTRINSIC-
Modifiable (footwear, training surface, workload)

Target Market(s)

Researchers and clinicians

Requirements
Must have
• A scientific feel
Nice to have
• Creative way to display the cumulative and interactive impact of risk factors
Should not have
• Too cartoon-ish or child-like feel

```html
<!DOCTYPE html>
<html lang="en">
<head>
<meta charset="utf-8">
<title>Risk Factors of Stress Fractures</title>
<link href="https://fonts.googleapis.com/css2?family=Montserrat:ital,wght@0,400;0,500;0,600;0,800;1,800&family=Fira+Sans:wght@600&family=Fira+Sans+Extra+Condensed:wght@600&display=swap" rel="stylesheet">
<style>
:root{
  --black:#000;
  --ink:#0d3a52;
  --cyan:#bfe6ec;
  --band:#5695a0;
  --deep-top:#1a2a34;
  --deep-bottom:#0a4f6b;
  --white:#fff;
  --grey:#7d7d7d;
}
*{box-sizing:border-box;margin:0;padding:0}
html,body{width:849px;height:1200px;overflow:hidden;background:var(--black)}
body{font-family:"Montserrat",sans-serif;color:var(--white);position:relative}
.hero{position:absolute;left:0;top:0;width:849px;height:520px;background:var(--black)}
.hero-figure{position:absolute;left:540px;top:0;width:309px;height:490px;
  background:radial-gradient(ellipse at 60% 45%,#8a6a5a 0%,#4a3128 45%,#000 80%)}
.title-rule{position:absolute;height:2px;background:var(--white)}
.title{position:absolute;left:68px;top:106px;font-weight:800;font-style:italic;font-size:35px;line-height:42px;letter-spacing:.5px}
.warning{position:absolute;left:130px;top:252px}
.headline{position:absolute;left:217px;top:248px;font-family:"Fira Sans",sans-serif;font-weight:600;font-size:23px;line-height:29px;color:var(--cyan)}
.definition{position:absolute;left:217px;top:337px;width:320px;font-size:15.5px;line-height:19.5px;font-weight:500;color:var(--cyan)}
.band{position:absolute;left:0;top:520px;width:849px;height:118px;background:var(--band)}
.portrait{position:absolute;top:502px;width:154px;height:154px;border-radius:50%}
.band-text{position:absolute;left:484px;top:543px;font-family:"Fira Sans Extra Condensed",sans-serif;font-weight:600;font-size:20px;line-height:24.5px;letter-spacing:.4px}
.factors{position:absolute;left:0;top:638px;width:849px;height:562px;background:linear-gradient(180deg,var(--deep-top) 0%,var(--deep-top) 18%,var(--deep-bottom) 100%)}
.frame{position:absolute;border:2px solid var(--white);border-top:none}
.frame-top{position:absolute;height:2px;background:var(--white)}
.group-title{position:absolute;border:2px solid var(--white);background:var(--deep-top);text-align:center;font-size:16px;font-weight:500;line-height:19px;padding-top:6px}
.group-label{position:absolute;text-align:center;font-size:13px;font-weight:500;line-height:17px;width:140px;margin-left:-70px}
.factor{position:absolute;width:100px;margin-left:-50px;text-align:center}
.disc{width:72px;height:72px;border-radius:50%;background:var(--white);margin:0 auto;display:flex;align-items:center;justify-content:center;color:#000}
.pill{display:inline-block;background:var(--white);color:var(--ink);border-radius:10px;margin-top:5px;font-size:12.5px;line-height:16px;padding:1px 10px;min-width:72px}
.pill.small{font-size:9px;line-height:10px;padding:4px 10px;border-radius:13px}
.yo{font-weight:800;font-size:26px;letter-spacing:-1px}
</style>
</head>
<body>
<section class="hero">
  <div class="hero-figure" role="img" aria-label="Anatomical rendering of a running leg with the tibia visible and a highlighted stress fracture site"></div>
  <div class="title-rule" style="left:69px;top:96px;width:276px"></div>
  <h1 class="title">RISK FACTORS<br>OF STRESS FRACTURES</h1>
  <div class="title-rule" style="left:130px;top:197px;width:475px"></div>
  <svg class="warning" width="58" height="54" viewBox="0 0 58 54" aria-label="Warning">
    <path d="M29 2 L56 51 L2 51 Z" fill="#bfe6ec" stroke="#bfe6ec" stroke-width="3" stroke-linejoin="round"/>
    <rect x="26.5" y="16" width="5" height="20" rx="2" fill="#000"/>
    <circle cx="29" cy="43" r="3" fill="#000"/>
  </svg>
  <h2 class="headline">The risk factors are<br>cumulative and interactive</h2>
  <p class="definition">A subjective clinical determination of the number of factors putting an athlete at risk along with thoughtful consideration regarding how all the risk factors interact with one another</p>
</section>

<section class="band"></section>
<div class="portrait" style="left:127px;background:linear-gradient(135deg,#e9e6e2,#8c7b6c)" role="img" aria-label="Portrait photo of a runner"></div>
<div class="portrait" style="left:217px;background:linear-gradient(135deg,#f1f1f1,#9a8676)" role="img" aria-label="Portrait photo of a female athlete running"></div>
<div class="portrait" style="left:303px;background:linear-gradient(135deg,#cfd3d6,#6d6a55)" role="img" aria-label="Portrait photo of a soldier in uniform"></div>
<p class="band-text">STRESS FRACTURES<br>ARE COMMON IN ATHLETES<br>AND MILITARY PERSONNEL</p>

<section class="factors">
  <div class="frame" style="left:11px;top:89px;width:656px;height:461px"></div>
  <div class="frame-top" style="left:11px;top:89px;width:255px"></div>
  <div class="frame-top" style="left:412px;top:89px;width:255px"></div>
  <div class="group-title" style="left:273px;top:63px;width:132px;height:52px">INTRINSIC<br>FACTORS</div>

  <div class="frame" style="left:680px;top:89px;width:158px;height:461px"></div>
  <div class="group-title" style="left:693px;top:63px;width:132px;height:52px">EXTRINSIC<br>FACTORS</div>

  <p class="group-label" style="left:120px;top:133px">Non-modifiable</p>
  <p class="group-label" style="left:385px;top:133px">Modifiable</p>
  <p class="group-label" style="left:602px;top:124px">Unclear<br>if modifiable</p>
  <p class="group-label" style="left:758px;top:133px">Modifiable</p>
</section>

<!-- row 1 -->
<div class="factor" style="left:71px;top:804px"><div class="disc">
  <svg width="44" height="44" viewBox="0 0 44 44" fill="none" stroke="#000" stroke-width="2"><circle cx="17" cy="20" r="8"/><circle cx="24" cy="18" r="8"/><path d="M17 28v12M12 35h10M30 12l8-8M32 4h6v6"/></svg>
</div><span class="pill">SEX</span></div>
<div class="factor" style="left:169px;top:804px"><div class="disc">
  <svg width="46" height="40" viewBox="0 0 46 40">
    <g fill="#000"><rect x="3" y="6" width="4.5" height="10" rx="2"/><rect x="8" y="4" width="4.5" height="12" rx="2"/><rect x="13" y="5" width="4.5" height="11" rx="2"/><rect x="3" y="13" width="17" height="12" rx="3"/><rect x="6" y="24" width="11" height="14"/></g>
    <g fill="#7d7d7d"><rect x="25" y="6" width="4.5" height="10" rx="2"/><rect x="30" y="4" width="4.5" height="12" rx="2"/><rect x="35" y="5" width="4.5" height="11" rx="2"/><rect x="25" y="13" width="17" height="12" rx="3"/><rect x="28" y="24" width="11" height="14"/></g>
  </svg>
</div><span class="pill">RACE</span></div>
<div class="factor" style="left:286px;top:804px"><div class="disc">
  <svg width="40" height="44" viewBox="0 0 40 44" fill="#000"><rect x="7" y="4" width="2" height="14"/><rect x="11" y="4" width="2" height="14"/><rect x="15" y="4" width="2" height="14"/><rect x="10" y="16" width="4" height="26" rx="2"/><ellipse cx="29" cy="12" rx="5" ry="9"/><rect x="27" y="18" width="4" height="24" rx="2"/></svg>
</div><span class="pill">NUTRITION</span></div>
<div class="factor" style="left:384px;top:804px"><div class="disc">
  <svg width="50" height="46" viewBox="0 0 50 46">
    <g fill="#000"><path d="M8 3l4 8-3 1z"/><path d="M22 1h4l-1 10h-2z"/><path d="M40 3l2 2-6 7-1-1z"/><path d="M2 14l6 2-1 2-6-2z"/></g>
    <path d="M10 30c-4-6 2-12 8-11 2-4 9-5 12-1 5-2 11 2 10 7 4 3 2 10-3 10-1 4-8 6-12 3-4 3-11 1-11-3-3 0-5-3-4-5z" fill="#000"/>
    <path d="M16 26c3 0 4 3 7 2M26 24c2 2 5 1 7 3M18 34c3-2 6 0 9-1M30 33c2-1 4 0 6-1" stroke="#fff" stroke-width="1.2" fill="none"/>
  </svg>
</div><span class="pill">STRESS</span></div>
<div class="factor" style="left:484px;top:804px"><div class="disc">
  <svg width="46" height="46" viewBox="0 0 46 46" fill="none" stroke="#000" stroke-linecap="round">
    <circle cx="19" cy="5" r="3.5" fill="#000" stroke="none"/>
    <path d="M19 10 L20 18" stroke-width="4"/>
    <path d="M12 42 C10 26 18 16 26 18 C34 20 38 30 38 42" stroke-width="5"/>
    <path d="M8 42h8M34 42h8" stroke-width="3"/>
  </svg>
</div><span class="pill">FLEXIBILITY</span></div>
<div class="factor" style="left:603px;top:804px"><div class="disc">
  <svg width="46" height="46" viewBox="0 0 46 46" fill="none" stroke="#000" stroke-linecap="round" stroke-linejoin="round">
    <path d="M8 24 V10 Q8 5 13 5 H33 Q38 5 38 10 V30 Q38 36 32 36 H28 L26 42" stroke-width="6"/>
    <path d="M8 24 Q8 30 14 30 M14 14 Q20 10 24 16 Q28 22 32 16" stroke-width="3.5"/>
  </svg>
</div><span class="pill" style="font-size:10.5px">GUT HEALTH</span></div>
<div class="factor" style="left:758px;top:807px"><div class="disc">
  <svg width="52" height="24" viewBox="0 0 52 24" fill="#000"><path d="M2 14 L30 12 L38 2 L50 4 L50 18 L2 18 Z"/><rect x="2" y="19" width="48" height="3"/></svg>
</div><span class="pill">FOOTWEAR</span></div>

<!-- row 2 -->
<div class="factor" style="left:71px;top:925px"><div class="disc">
  <svg width="48" height="40" viewBox="0 0 48 40" fill="none" stroke="#000" stroke-width="2.5" stroke-linecap="round">
    <g transform="rotate(-25 24 20)">
      <path d="M2 20 C8 8 14 8 20 20 S32 32 38 20 S44 10 46 12"/>
      <path d="M2 20 C8 32 14 32 20 20 S32 8 38 20 S44 30 46 28"/>
      <path d="M8 12v16M14 12v16M26 12v16M32 12v16M42 15v10" stroke-width="1.6"/>
    </g>
  </svg>
</div><span class="pill">GENETICS</span></div>
<div class="factor" style="left:169px;top:925px"><div class="disc"><span class="yo">Y.O</span></div><span class="pill">AGE</span></div>
<div class="factor" style="left:286px;top:925px"><div class="disc">
  <svg width="48" height="48" viewBox="0 0 48 48"><rect x="4" y="17" width="40" height="14" rx="7" fill="#000" transform="rotate(-45 24 24)"/><rect x="17" y="19" width="14" height="10" fill="#fff" transform="rotate(-45 24 24)"/></svg>
</div><span class="pill small">RECOVERY<br>STRATEGIES</span></div>
<div class="factor" style="left:384px;top:925px"><div class="disc">
  <svg width="48" height="40" viewBox="0 0 48 40"><path d="M12 2 L4 22 L10 22 L6 38 L18 16 L12 16 L16 2 Z" fill="#000"/><text x="20" y="27" font-family="Montserrat,sans-serif" font-weight="600" font-size="10" fill="#000">LOW</text></svg>
</div><span class="pill small">ENERGY<br>DEFICIENCY</span></div>
<div class="factor" style="left:484px;top:925px"><div class="disc">
  <svg width="46" height="50" viewBox="0 0 46 50" fill="none" stroke="#000" stroke-linecap="round" stroke-linejoin="round">
    <circle cx="28" cy="6" r="4" fill="#000" stroke="none"/>
    <path d="M26 12 L22 28" stroke-width="6"/>
    <path d="M25 14 L16 20 L10 18 M26 15 L32 22 L38 20" stroke-width="3"/>
    <path d="M22 28 L30 36 L28 46 M22 28 L14 36 L4 36" stroke-width="4"/>
  </svg>
</div><span class="pill small">BIO<br>MECHANICS</span></div>
<div class="factor" style="left:758px;top:929px"><div class="disc">
  <svg width="52" height="44" viewBox="0 0 52 44"><text x="26" y="12" text-anchor="middle" font-family="Montserrat,sans-serif" font-weight="600" font-size="10" fill="#000">OVER !</text><rect x="4" y="24" width="4" height="12" fill="#000"/><rect x="9" y="20" width="6" height="20" fill="#000"/><rect x="15" y="28" width="22" height="4" fill="#000"/><rect x="37" y="20" width="6" height="20" fill="#000"/><rect x="44" y="24" width="4" height="12" fill="#000"/></svg>
</div><span class="pill">WORKLOAD</span></div>

<!-- row 3 -->
<div class="factor" style="left:71px;top:1044px"><div class="disc">
  <svg width="24" height="52" viewBox="0 0 24 52" fill="#000">
    <circle cx="12" cy="5" r="4.5"/>
    <rect x="6" y="11" width="12" height="19" rx="3"/>
    <rect x="1.5" y="12" width="4" height="17" rx="2"/><rect x="18.5" y="12" width="4" height="17" rx="2"/>
    <rect x="6.5" y="29" width="5" height="22" rx="2"/><rect x="12.5" y="29" width="5" height="22" rx="2"/>
  </svg>
</div><span class="pill small">ANATOMICAL<br>STRUCTURE</span></div>
<div class="factor" style="left:169px;top:1044px"><div class="disc">
  <svg width="56" height="50" viewBox="0 0 56 50">
    <path d="M2 6 L14 2 L34 28 L24 36 Z" fill="#000"/>
    <path d="M24 30 L36 22 L48 34 Q52 38 48 42 L34 44 Q28 44 26 40 Z" fill="#fff" stroke="#000" stroke-width="3" stroke-linejoin="round"/>
    <path d="M30 30 L40 40 M34 26 L44 36" stroke="#000" stroke-width="1.5"/>
  </svg>
</div><span class="pill small">PRIOR BONE<br>STRESS INJURY</span></div>
<div class="factor" style="left:286px;top:1044px"><div class="disc">
  <svg width="54" height="54" viewBox="0 0 54 54" fill="none" stroke="#000" stroke-width="1.8" stroke-linecap="round">
    <path d="M12 50 Q8 36 10 24 Q11 10 16 4 Q22 2 26 6 Q30 16 28 30 Q26 42 22 50 Z"/>
    <path d="M14 8v10M18 6v12M22 7v12M25 10v10M14 22h12M16 28v16M20 28v16"/>
    <path d="M40 12v14M35 21l5 6 5-6" stroke-width="2.5"/>
  </svg>
</div><span class="pill small">MUSCLE<br>FATIGUE</span></div>
<div class="factor" style="left:384px;top:1044px"><div class="disc">
  <svg width="54" height="54" viewBox="0 0 54 54" fill="none" stroke="#000" stroke-width="1.8" stroke-linecap="round">
    <path d="M12 50 Q8 36 10 24 Q11 10 16 4 Q22 2 26 6 Q30 16 28 30 Q26 42 22 50 Z"/>
    <path d="M14 8v10M18 6v12M22 7v12M25 10v10M14 22h12M16 28v16M20 28v16"/>
    <path d="M38 6v12M32 12h12M44 18v8M40 22h8" stroke-width="3.5" stroke-linecap="butt"/>
  </svg>
</div><span class="pill small">MUSCLE<br>STRENGTH</span></div>
<div class="factor" style="left:758px;top:1048px"><div class="disc">
  <svg width="52" height="14" viewBox="0 0 52 14"><rect x="1" y="1" width="50" height="12" fill="none" stroke="#000" stroke-width="2"/><path d="M6 12 L10 2 M12 12 L16 2 M18 12 L22 2 M24 12 L28 2 M30 12 L34 2 M36 12 L40 2 M42 12 L46 2" stroke="#000" stroke-width="2"/></svg>
</div><span class="pill small">TRAINING<br>SURFACE</span></div>
</body>
</html>
```